The Balanced Plate Hour with Dan Orrick.

I'm launching this podcast on health and wellness and I want to be take serious. That starts with a great design. There's too much contradiction out there about what is and isn't healthy. I want my podcast to be a resource that people can rely upon. I want my face in it and I want it to pop with colors that catch the eye. I want It clean and crisp. I was also thinking of experimenting with an animated photo of me as well. What ever looks best.

Industry/Entity Type

Health And Wellness

Font styles to use
Sans Serif

Requirements
Must have
• My face and or body.

```html
<!DOCTYPE html>
<html lang="en">
<head>
<meta charset="utf-8">
<title>The Balanced Plate Hour with Dan Orrick</title>
<link rel="stylesheet" href="https://fonts.googleapis.com/css2?family=Chakra+Petch:wght@500;600&family=Exo+2:wght@600&display=swap">
<style>
  :root {
    --slate: #575667;
    --hair: #22212d;
    --skin-light: #d9dad3;
    --skin-mid: #9c9ca0;
    --skin-shadow: #4a4957;
    --shirt: #1f1e29;
    --cream: #eef0e6;
  }
  html, body {
    margin: 0;
    padding: 0;
    width: 1200px;
    height: 1200px;
    overflow: hidden;
    background: var(--slate);
  }
  .cover {
    position: relative;
    width: 1200px;
    height: 1200px;
    background: var(--slate);
    overflow: hidden;
  }
  .host-portrait {
    position: absolute;
    left: 420px;
    top: 0;
    width: 780px;
    height: 1200px;
    background:
      radial-gradient(ellipse 26% 22% at 62% 46%, var(--skin-light) 0%, var(--skin-mid) 55%, rgba(156,156,160,0) 100%),
      radial-gradient(ellipse 34% 30% at 62% 48%, rgba(120,120,128,0.95) 0%, rgba(87,86,103,0) 100%),
      radial-gradient(ellipse 38% 18% at 62% 14%, var(--hair) 0%, rgba(34,33,45,0.85) 55%, rgba(34,33,45,0) 100%),
      radial-gradient(ellipse 70% 38% at 78% 100%, var(--shirt) 0%, var(--shirt) 60%, rgba(31,30,41,0) 100%);
    -webkit-mask-image: linear-gradient(90deg, transparent 0%, #000 22%);
    mask-image: linear-gradient(90deg, transparent 0%, #000 22%);
  }
  .host-credit {
    position: absolute;
    left: 74px;
    top: 56px;
    color: var(--cream);
    font-family: "Chakra Petch", sans-serif;
    text-transform: uppercase;
  }
  .host-credit .with {
    display: block;
    font-weight: 600;
    font-size: 20px;
    letter-spacing: 2px;
  }
  .host-credit .host-name {
    display: block;
    font-weight: 600;
    font-size: 104px;
    line-height: 96px;
    letter-spacing: 5px;
    margin-top: 18px;
    margin-left: 10px;
  }
  .show-title {
    position: absolute;
    left: 24px;
    top: 742px;
    margin: 0;
    color: var(--cream);
    font-family: "Exo 2", sans-serif;
    font-weight: 600;
    text-transform: uppercase;
  }
  .show-title span { display: block; }
  .show-title .the { font-size: 72px;  line-height: 84px;  letter-spacing: 9px; }
  .show-title .big { font-size: 138px; line-height: 124px; letter-spacing: 2px; }
  .show-title .mid { font-size: 80px;  line-height: 92px;  letter-spacing: 8px; }
  .show-title .end { font-size: 146px; line-height: 136px; letter-spacing: 8px; }
</style>
</head>
<body>
  <main class="cover">
    <div class="host-portrait" role="img" aria-label="Black and white portrait of host Dan Orrick, head and shoulders, dark t-shirt, looking at the viewer"></div>

    <div class="host-credit">
      <span class="with">With</span>
      <span class="host-name">Dan<br>Orrick</span>
    </div>

    <h1 class="show-title">
      <span class="the">The</span>
      <span class="big">Balanced</span>
      <span class="mid">Plate</span>
      <span class="end">Hour</span>
    </h1>
  </main>
</body>
</html>
```